Sales Funnel Infographic

Attached is our sale funnel graphic. We want to rebuild it from scratch as a vector Infographic, preferably .ai file. It will be used on our website & all sales collateral - both web and print.

This is a cornerstone of our marketing to illustrate to our potential clients what we do. We build sales engines for startup companies who don't yet have a department for sales and/or a systematic strategy for sales & marketing.

We will keep the basic funnel design, the copy, the order & relationships - by relationships I mean the arrows/connections between the pieces.

Examples of funnels I like:

http://www.plovrane.com/wp-content/uploads/2012/02/inbound-marketing-funnel.jpg

http://www.quelmarin.com/~/media/ideas%20blog%20images/video-for-sales-infographic.ashx

http://gravelmintyarchive.files.pagetrellis.com/2014/01/3d-funnel-design_01.jpg?w=700

Here's our website: http://ferncrow.com

our colors: corporate blue: #00144F
font: Titillium Web from Google Fonts

Final size should be 9x16 ratio including white space = tall version of HD widescreen

Target Market(s)

Funded businesses and silicon valley startups who are looking to hire us to create a sales engine for them.

Industry/Entity Type

Marketing

Font styles to use
Sans Serif

Requirements
Must have
• Vector .ai format
Basic Funnel Shape
All copy from attachment & relationships
white background
Nice to have
• optional color background
Should not have
• super-tall format

```html
<!DOCTYPE html>
<html lang="en">
<head>
<meta charset="utf-8">
<title>STEADY Growth Engine</title>
<link href="https://fonts.googleapis.com/css2?family=Titillium+Web:wght@400;600;700&display=swap" rel="stylesheet">
<style>
  :root {
    --navy: #0f3147;
    --subtitle: #3d6b8e;
    --step1-light: #5b8db5;
    --step1-dark: #3d6e98;
    --step2: #e63e6a;
    --step2-dark: #c8163f;
    --step3: #e0862f;
    --step3-light: #f7941d;
    --step4: #c2a530;
    --arrow: #3b8bd0;
    --band: #c8dcf0;
    --qualify: #1e8c6c;
    --develop: #c81f45;
    --close: #f7941d;
    --growth: #e2c22d;
    --ink: #1a1a1a;
    --white: #ffffff;
  }
  * { margin: 0; padding: 0; box-sizing: border-box; }
  html, body { width: 675px; height: 1200px; overflow: hidden; background: var(--white); }
  .canvas {
    position: relative; width: 675px; height: 1200px; overflow: hidden;
    font-family: "Titillium Web", sans-serif; color: var(--ink);
  }
  .title { position: absolute; top: 22px; width: 100%; text-align: center;
    font-size: 44px; font-weight: 700; color: var(--navy); line-height: 60px; }
  .subtitle { position: absolute; top: 102px; width: 100%; text-align: center;
    font-size: 21px; font-weight: 700; color: var(--subtitle); line-height: 28px; }
  .rule { position: absolute; top: 155px; left: 0; width: 675px; height: 18px; background: var(--navy); }
  .graphic { position: absolute; top: 0; left: 0; }
  .step { position: absolute; left: 0; color: var(--white); font-size: 20px; font-weight: 600;
    line-height: 26px; padding-left: 26px; display: flex; align-items: center; }
  .step-1 { top: 218px; width: 363px; height: 35px; background: var(--step1-light); }
  .step-2 { top: 282px; width: 302px; height: 92px; background: var(--step2); }
  .step-3 { top: 391px; width: 302px; height: 92px; background: var(--step3); }
  .step-4 { top: 508px; width: 302px; height: 93px; background: var(--step4); }
  .stage-label { position: absolute; color: var(--white); font-size: 20px;
    display: flex; align-items: center; justify-content: center; }
  .label-vision { left: 363px; top: 218px; width: 178px; height: 35px; background: var(--step1-dark); }
  .label-strategy { left: 302px; top: 282px; width: 281px; height: 34px; background: var(--step2-dark); }
  .label-tools { left: 302px; top: 450px; width: 290px; height: 34px; background: var(--step3-light); }
  .label-demand { left: 320px; top: 539px; width: 250px; height: 30px; color: var(--ink); }
  .funnel-label { position: absolute; text-align: center; color: var(--ink); font-size: 26px; line-height: 34px; }
  .note { position: absolute; left: 25px; font-size: 19px; font-weight: 600; line-height: 26px; color: var(--ink); }
  .note-5 { top: 675px; }
  .note-6 { top: 859px; }
  .note-7 { top: 1024px; }
  .money { position: absolute; font-size: 22px; color: var(--ink); line-height: 28px; }
  .brand { position: absolute; top: 1120px; left: 400px; }
  .brand-name { font-size: 36px; font-weight: 400; color: var(--navy); line-height: 48px; }
</style>
</head>
<body>
<div class="canvas">
  <h1 class="title">STEADY Growth Engine:</h1>
  <p class="subtitle">A proven process to drive predictable revenue and growth.</p>
  <div class="rule"></div>

  <svg class="graphic" width="675" height="1200" viewBox="0 0 675 1200">
    <rect x="388" y="250" width="130" height="242" fill="var(--arrow)"/>
    <polygon points="298,490 582,490 452,636" fill="var(--arrow)"/>
    <polygon points="333,540 569,540 544,568 358,568" fill="var(--band)"/>
    <path d="M258,645 Q453,628 648,645 L617,722 Q453,735 290,722 Z" fill="var(--qualify)"/>
    <path d="M285,734 Q453,720 620,734 L593,805 Q453,817 313,805 Z" fill="var(--develop)"/>
    <path d="M310,822 Q453,810 593,822 L568,883 Q453,894 337,883 Z" fill="var(--close)"/>
    <path d="M340,940 Q453,926 565,940 L545,994 Q453,1004 362,994 Z" fill="var(--growth)"/>
    <g fill="none" stroke="var(--ink)" stroke-width="2.5" stroke-dasharray="10 7">
      <path d="M255,655 Q205,770 325,880"/>
      <path d="M183,963 L320,963"/>
      <path d="M340,912 L250,1025"/>
      <path d="M250,1025 L370,1042"/>
    </g>
  </svg>

  <div class="step step-1">1. Clarify vision, goals, values</div>
  <div class="stage-label label-vision">Vision &amp; Goals</div>
  <div class="step step-2">2. Develop, refine audience,<br>value prop, key messages,<br>differentiators, channels</div>
  <div class="stage-label label-strategy">Customer-Centric Strategy</div>
  <div class="step step-3">3. Optimize sales tools,<br>website, overview, pitch<br>deck, technologies</div>
  <div class="stage-label label-tools">Foundational Tools</div>
  <div class="step step-4">4. Prioritize &amp; execute<br>demand-gen<br>activities, measure, optimize</div>
  <div class="stage-label label-demand">Demand Generation</div>

  <div class="funnel-label" style="left:290px;top:668px;width:326px;">Qualify</div>
  <div class="funnel-label" style="left:313px;top:757px;width:280px;">Develop</div>
  <div class="funnel-label" style="left:337px;top:847px;width:231px;">Close</div>
  <div class="funnel-label" style="left:362px;top:955px;width:183px;font-size:21px;">Growth &amp; Scale</div>

  <div class="money" style="left:424px;top:898px;">$+V</div>
  <div class="money" style="left:384px;top:1021px;">$$$$$$$$$</div>

  <p class="note note-5">5. Develop, refine,<br>execute biz dev &amp;<br>sales process,<br>account<br>development,<br>team</p>
  <p class="note note-6">6. Past/current<br>client relations,<br>resell,<br>retention and<br>referrals, service</p>
  <p class="note note-7">7. Measure, optimize,<br>build capacity,<br>accelerate, scale</p>

  <div class="brand">
    <span class="brand-name">Ferncrow</span>
  </div>
</div>
</body>
</html>
```